Company Values Poster

Project Brief: Refinement of Brantow Core Values Visuals
Overview
Brantow Power Controls Pty Ltd is seeking a designer to refine and improve the visual presentation of our company core values, ensuring they are clear, modern, scalable, and aligned with our existing brand identity.

We are not looking for a complete rebrand. The objective is to elevate and sharpen our current values artwork so it works consistently across
internal presentations and onboarding material, signage, decals, and digital assets.

Scope of Work
The designer will be required to:
- Refine and modernise our existing core values icons and layout
- Improve visual consistency, spacing, hierarchy, and legibility
- Ensure icons and typography scale cleanly for both digital and print
- Maintain strong alignment with our current branding, colours, fonts, and tone
- Provide a polished, professional, engineering-led aesthetic
- Core Values (Content to Remain Conceptually Consistent)

The following values already exist and should remain conceptually intact, but may be visually refined:

Always Evolving
Stay curious, adapt, and share to grow.

Straight Talk
Be real. No triangles, no bullshit.

Respect Builds Trust
Value people and put them first.

Do It Once, Do It Right
Put your name on it.

Safety First, Own It
We prioritise the safety of our people and our customers.

One Team
One standard, no passengers.

Brand Alignment (Critical)
- Designs must align strictly with our existing brand guidelines and visual language.
We will provide:
- Current core values design (requires resolution and layout improvement)
- Brantow brand specifications (colours, fonts, logo usage)
- Brantow-Brand-Specifications
- Primary Brantow logo
- Brantow logo mark

Key brand attributes:
- Engineering-led
- Practical, no-nonsense
- Quality, safety, and trust focused
- Industrial / infrastructure context (not consumer or tech-startup style)
- Style Direction
- Clean, modern, and confident
- Strong iconography with clear meaning
- Avoid gimmicks, gradients, or over-complex illustration
- Must feel appropriate for critical electrical infrastructure, heavy industry, and energy projects
- Consistent line weights and icon geometry preferred
Deliverables
- Refined core values layout (full set)
- Individual icon files for each value
- High-resolution assets suitable for: Web, Print, Presentations, Editable source files

```html
<!DOCTYPE html>
<html lang="en">
<head>
<meta charset="utf-8">
<title>Brantow Core Values</title>
<link rel="stylesheet" href="https://fonts.googleapis.com/css2?family=Russo+One&family=Montserrat:wght@400&display=swap">
<style>
  :root {
    --brand-green: #146333;
    --brand-red: #e32b2b;
    --ink: #232323;
    --paper: #ffffff;
    --paper-shade: #ececec;
    --stage: #dcdcdc;
  }
  html, body {
    margin: 0;
    padding: 0;
    width: 1063px;
    height: 1200px;
    overflow: hidden;
    background: var(--stage);
  }
  .values-board {
    position: absolute;
    left: 0;
    top: 290px;
    width: 1063px;
    height: 620px;
    display: block;
  }
  .heading { font-family: "Russo One", sans-serif; font-size: 31px; text-anchor: middle; letter-spacing: 1px; }
  .heading--red { fill: var(--brand-red); }
  .heading--green { fill: var(--brand-green); }
  .summary { font-family: "Montserrat", sans-serif; font-size: 22px; fill: var(--ink); text-anchor: middle; }
  .wordmark { font-family: "Russo One", sans-serif; font-size: 78px; fill: var(--brand-green); text-anchor: middle; letter-spacing: 2px; }
  .title { font-family: "Russo One", sans-serif; font-size: 70px; letter-spacing: 2px; }
  .title__accent { fill: var(--brand-green); }
  .title__main { fill: var(--ink); }
  .track { fill: none; stroke: var(--ink); stroke-width: 22; stroke-linecap: round; }
  .node { fill: var(--brand-red); }
  .rule--green { stroke: var(--brand-green); stroke-width: 2; }
  .rule--red { stroke: var(--brand-red); stroke-width: 2; }
  .icon--green { fill: var(--brand-green); }
  .icon--red { fill: var(--brand-red); }
  .bar { fill: var(--ink); }
</style>
</head>
<body>
<svg class="values-board" viewBox="0 988 1811 1056" xmlns="http://www.w3.org/2000/svg" aria-label="Brantow core values">
  <defs>
    <linearGradient id="paper-fade" x1="0" y1="0" x2="0" y2="1">
      <stop offset="0" stop-color="#ffffff"/>
      <stop offset="0.6" stop-color="#f3f3f3"/>
      <stop offset="1" stop-color="#e6e6e6"/>
    </linearGradient>
  </defs>

  <!-- board background -->
  <rect x="0" y="988" width="1811" height="1056" fill="url(#paper-fade)"/>

  <!-- header band with name tab -->
  <rect x="0" y="988" width="1811" height="102" fill="var(--brand-green)"/>
  <rect x="680" y="1024" width="451" height="130" rx="42" fill="var(--paper)"/>
  <text class="wordmark" x="905" y="1116">BRANTOW</text>

  <!-- value track -->
  <path class="track" d="M190 1413 H180 Q140 1413 140 1453 V1630 Q140 1670 180 1670 H355 Q395 1670 395 1630 V1472"/>
  <path class="track" d="M440 1424 H610 Q650 1424 650 1464 V1620"/>
  <path class="track" d="M700 1670 H865 Q905 1670 905 1630 V1472"/>
  <path class="track" d="M955 1424 H1120 Q1160 1424 1160 1464 V1620"/>
  <path class="track" d="M1210 1670 H1375 Q1415 1670 1415 1630 V1472"/>
  <path class="track" d="M1466 1424 H1635 Q1675 1424 1675 1464 V1645 Q1675 1685 1635 1685 H1620"/>

  <circle class="node" cx="395" cy="1424" r="11"/>
  <circle class="node" cx="650" cy="1670" r="11"/>
  <circle class="node" cx="905" cy="1424" r="11"/>
  <circle class="node" cx="1160" cy="1670" r="11"/>
  <circle class="node" cx="1417" cy="1424" r="11"/>

  <!-- value icons -->
  <rect class="icon--green" x="217" y="1478" width="100" height="130" rx="22" role="img" aria-label="Icon: open hands holding an infinity loop with upward arrows"/>
  <rect class="icon--red" x="476" y="1496" width="94" height="94" rx="20" role="img" aria-label="Icon: two figures facing each other with speech bubbles"/>
  <rect class="icon--green" x="728" y="1482" width="100" height="122" rx="22" role="img" aria-label="Icon: two figures shaking hands inside a gear"/>
  <rect class="icon--red" x="995" y="1488" width="80" height="110" rx="20" role="img" aria-label="Icon: hand pressing a check mark"/>
  <rect class="icon--green" x="1242" y="1492" width="96" height="100" rx="22" role="img" aria-label="Icon: hands protecting a shield"/>
  <rect class="icon--red" x="1497" y="1494" width="96" height="96" rx="22" role="img" aria-label="Icon: group of people around a gear"/>

  <!-- upper values -->
  <text class="heading heading--red" x="522" y="1296">STRAIGHT</text>
  <text class="heading heading--red" x="522" y="1326">TALK</text>
  <line class="rule--green" x1="433" y1="1337" x2="613" y2="1337"/>
  <text class="summary" x="522" y="1366">Be real. No triangles,</text>
  <text class="summary" x="522" y="1391">no bullshit.</text>

  <text class="heading heading--red" x="1033" y="1296">DO IT ONCE,</text>
  <text class="heading heading--red" x="1033" y="1326">DO IT RIGHT</text>
  <line class="rule--green" x1="943" y1="1337" x2="1123" y2="1337"/>
  <text class="summary" x="1033" y="1366">Put your name on it.</text>

  <text class="heading heading--red" x="1545" y="1296">ONE</text>
  <text class="heading heading--red" x="1545" y="1326">TEAM</text>
  <line class="rule--green" x1="1455" y1="1337" x2="1635" y2="1337"/>
  <text class="summary" x="1545" y="1366">One standard, no</text>
  <text class="summary" x="1545" y="1391">passengers.</text>

  <!-- lower values -->
  <text class="heading heading--green" x="266" y="1731">ALWAYS</text>
  <text class="heading heading--green" x="266" y="1761">EVOLVING</text>
  <line class="rule--red" x1="176" y1="1772" x2="356" y2="1772"/>
  <text class="summary" x="266" y="1802">Stay curious, adapt, and</text>
  <text class="summary" x="266" y="1827">share to grow.</text>

  <text class="heading heading--green" x="777" y="1731">RESPECT</text>
  <text class="heading heading--green" x="777" y="1761">BUILDS TRUST</text>
  <line class="rule--red" x1="687" y1="1772" x2="867" y2="1772"/>
  <text class="summary" x="777" y="1802">Value people and put</text>
  <text class="summary" x="777" y="1827">them first.</text>

  <text class="heading heading--green" x="1290" y="1731">SAFETY FIRST,</text>
  <text class="heading heading--green" x="1290" y="1761">OWN IT</text>
  <line class="rule--red" x1="1200" y1="1772" x2="1380" y2="1772"/>
  <text class="summary" x="1290" y="1802">We prioritise the</text>
  <text class="summary" x="1290" y="1827">safety of our people</text>
  <text class="summary" x="1290" y="1852">and our customers.</text>

  <!-- footer title -->
  <rect class="bar" x="0" y="1950" width="536" height="32" rx="16"/>
  <circle class="node" cx="562" cy="1966" r="16"/>
  <text class="title" x="910" y="1990" text-anchor="middle"><tspan class="title__accent">CORE</tspan> <tspan class="title__main">VALUES</tspan></text>
  <circle class="node" cx="1250" cy="1966" r="16"/>
  <rect class="bar" x="1276" y="1950" width="560" height="32" rx="16"/>
</svg>
</body>
</html>
```